Business card design needed

This is a new business and a unique service.
The market is academic staff at universities in Australia.
The services include workshops, seminars, individual research planning, individual support to develop grant applications for major funding. I will travel to work with people or work electronically with individuals. I have a highly successful track record and am known in many universities for work done in the past.

Target Market(s)

university professorial staff and junior academic staff in australia

Industry/Entity Type

Travel

Contact Information for Business Card

The Scholar Summit
Charting Roads to Scholar Funding

Dr Lorna P Quist

www.scholarsummit.com.au
E: info@scholarsummit.com.au
Ph: 0487 620843

Requirements
Must have
• I want a classic simple design. Colours - clean shades of blue with a contrast (not browns or orange).
I want to see line used as the primary feature, diagonal or other acute angles through part of the card.
Fonts should be crisp, angular and highly readable. Use upper and lower case in all text (except email and web address)
A simple logo based on TSS would be good.
Card can be designed vertically if the design works best that way.

```html
<!DOCTYPE html>
<html lang="en">
<head>
<meta charset="utf-8">
<title>The Scholar Summit – Business Card</title>
<link rel="stylesheet" href="https://fonts.googleapis.com/css2?family=Open+Sans:wght@400;700&display=swap">
<style>
  :root {
    --backdrop: #e6e8ec;
    --navy-deep: #142a7e;
    --navy: #1f3c96;
    --blue-light: #4a78c4;
    --paper: #f4f5f7;
    --paper-shade: #dcdfe4;
    --ink: #222833;
    --ink-soft: #3a3f48;
    --white: #ffffff;
  }
  * { margin: 0; padding: 0; box-sizing: border-box; }
  html, body {
    width: 1200px; height: 900px; overflow: hidden;
    background: var(--backdrop);
    font-family: "Open Sans", "Myriad Pro", sans-serif;
  }
  .sheet {
    width: 1200px; height: 900px;
    display: flex; align-items: center; justify-content: center; gap: 40px;
  }
  .card {
    position: relative; width: 540px; height: 310px; overflow: hidden;
    box-shadow: 0 6px 18px rgba(20, 30, 60, 0.25);
  }
  .card-edge { position: absolute; inset: 0; width: 100%; height: 100%; }

  /* Front */
  .card-front {
    background: linear-gradient(120deg, var(--navy-deep) 0%, var(--navy) 35%, var(--blue-light) 55%, var(--navy) 75%, var(--navy-deep) 100%);
  }
  .card-front .brand {
    position: absolute; left: 84px; top: 124px;
    color: var(--white); font-weight: 700; font-size: 26px; letter-spacing: 0.5px;
  }
  .card-front .tagline {
    position: absolute; left: 84px; top: 164px;
    color: var(--white); font-size: 18px;
  }

  /* Back */
  .card-back {
    background: linear-gradient(120deg, var(--paper-shade) 0%, var(--paper) 40%, var(--white) 55%, var(--paper) 70%, var(--paper-shade) 100%);
  }
  .card-back .brand {
    position: absolute; left: 42px; top: 70px;
    color: var(--navy-deep); font-weight: 700; font-size: 17px; letter-spacing: 0.4px;
  }
  .card-back .holder {
    position: absolute; right: 42px; top: 126px; text-align: right; color: var(--ink);
  }
  .card-back .holder-name { font-size: 22px; line-height: 30px; }
  .card-back .holder-role { font-size: 16px; line-height: 24px; }
  .card-back .contact {
    position: absolute; left: 42px; top: 210px;
    list-style: none; color: var(--ink-soft); font-size: 16px; line-height: 25px;
  }
  .card-back .contact b { color: var(--navy-deep); }
</style>
</head>
<body>
<main class="sheet">

  <section class="card card-front" aria-label="Card front">
    <svg class="card-edge" viewBox="0 0 540 310" preserveAspectRatio="none" aria-hidden="true">
      <defs>
        <linearGradient id="frontSweep" x1="0" y1="0" x2="1" y2="0">
          <stop offset="0" stop-color="#0f2070"/>
          <stop offset="0.35" stop-color="#d6dcef"/>
          <stop offset="0.7" stop-color="#ffffff"/>
          <stop offset="1" stop-color="#ffffff" stop-opacity="0.9"/>
        </linearGradient>
      </defs>
      <polygon points="0,0 540,0 540,2 160,50 0,30" fill="url(#frontSweep)" opacity="0.95"/>
      <polygon points="0,30 160,50 540,2 540,6 160,54 0,34" fill="#0f2070" opacity="0.35"/>
    </svg>
    <div class="brand">The Scholar Summit</div>
    <div class="tagline">Charting Roads to Scholar Funding</div>
  </section>

  <section class="card card-back" aria-label="Card back">
    <svg class="card-edge" viewBox="0 0 540 310" preserveAspectRatio="none" aria-hidden="true">
      <defs>
        <linearGradient id="backSweep" x1="0" y1="0" x2="1" y2="0">
          <stop offset="0" stop-color="#ffffff" stop-opacity="0"/>
          <stop offset="0.2" stop-color="#9aa7cf"/>
          <stop offset="0.45" stop-color="#1f3c96"/>
          <stop offset="1" stop-color="#142a7e"/>
        </linearGradient>
      </defs>
      <polygon points="20,0 540,0 540,4 160,50 20,44" fill="url(#backSweep)"/>
    </svg>
    <div class="brand">The Scholar Summit</div>
    <div class="holder">
      <div class="holder-name">Dr Lorna P Quist</div>
      <div class="holder-role">Charting Roads to Scholar Funding</div>
    </div>
    <ul class="contact">
      <li>www.scholarsummit.com.au</li>
      <li><b>E:</b> info@scholarsummit.com.au</li>
      <li><b>P:</b> 0487 620843</li>
    </ul>
  </section>

</main>
</body>
</html>
```